Business Card for a finance professional

I need a business card design to introduce myself to a professional networking (mainly banks) and potential companies to hire and remember me. I would like to use black, grey, white and maybe gold/silver colors and maybe something with my initials(R L F P T). The final design should communicate seriousness, profissionalism and something innovative.

The basic informations in the card are: Name, e-mail, phone number and trabnet. (I'm thinking to put some directly short link to my trabnet account or maybe some app - non QR Code - to add my contacts to a phone directly.)

My name is Mariana Lopes Ferreira Pinto dos Reis (I prefer to use only 'Mariana Lopes' or 'Mariana Reis' but i'm open to other suggestions) and I have 26 years old (just if it helps to build based in my age).
Updates

Dear designers, I wish to thank your participation in this project! It was very difficult to choose one! Thank your for your work! Best regards and success. Mariana

Target Market(s)

Potential hires and big companies.

Industry/Entity Type

Finance

Requirements
Must have
• The informations required at the business card are:
Name: Mariana Lopes F. P. dos Reis
Email: mariana.lop.reis@quellomail.com
Phone: +55 61 8493 5710
TrabNet: http://br.trabnet-perfis.com/in/marianalr/
Nice to have
• Modern and innovative look.
I suggest to use the colors black, grey, white, gold and/or silver, but I'm open to other colors.
Should not have
• A message showing that I need to be hired. It's more to "know me and remember me" than "hire me please".

```html
<!DOCTYPE html>
<html lang="pt">
<head>
<meta charset="utf-8">
<title>Mariana Lopes — Cartão de visita</title>
<link href="https://fonts.googleapis.com/css2?family=Arimo:wght@400;700&display=swap" rel="stylesheet">
<style>
  :root {
    --backdrop: #e2e2e2;
    --card: #ffffff;
    --ink: #2b2b2b;
    --ink-soft: #3a3a3a;
    --rule-grey: #b5b5b5;
    --band-black: #1a1a1a;
    --band-line: #8c8c8c;
  }
  * { margin: 0; padding: 0; box-sizing: border-box; }
  html, body {
    width: 1200px; height: 920px; overflow: hidden;
    background: var(--backdrop);
    font-family: "Arimo", Arial, sans-serif;
    color: var(--ink);
  }
  .canvas { position: relative; width: 1200px; height: 920px; }

  .card { position: absolute; background: var(--card); }
  .card--front { left: 105px; top: 87px; width: 620px; height: 353px; }
  .card--back  { left: 490px; top: 482px; width: 628px; height: 358px; overflow: hidden; }

  .monogram {
    position: absolute;
    font-family: "Arimo", Arial, sans-serif;
    font-weight: 400;
    color: var(--ink);
    white-space: nowrap;
    line-height: 1;
  }
  .card--front .monogram {
    left: 0; width: 100%; top: 153px;
    text-align: center;
    font-size: 46px; letter-spacing: 12px;
    transform: translateX(-2px);
  }
  .card--back .monogram {
    left: 36px; width: 258px; top: 158px;
    text-align: center;
    font-size: 40px; letter-spacing: 10px;
  }

  .profile-link {
    position: absolute;
    display: flex; align-items: center; gap: 8px;
    font-size: 14px; color: var(--ink-soft);
  }
  .card--front .profile-link { left: 215px; top: 308px; }
  .icon-square { width: 14px; height: 14px; background: var(--ink); border-radius: 2px; flex: none; }

  .divider {
    position: absolute; left: 327px; top: 113px; width: 1px; height: 132px;
    background: linear-gradient(to bottom, transparent, var(--rule-grey) 25%, var(--rule-grey) 75%, transparent);
  }

  .identity { position: absolute; left: 357px; top: 114px; }
  .identity__name { font-size: 18px; font-weight: 700; line-height: 22px; color: var(--ink); }
  .identity__surname { font-size: 18px; font-weight: 400; line-height: 22px; color: var(--ink-soft); }

  .contacts { position: absolute; left: 357px; top: 176px; list-style: none; font-size: 14px; color: var(--ink-soft); }
  .contacts li { display: flex; align-items: center; gap: 8px; height: 20px; }
  .contacts li.contacts__profile { margin-top: 12px; }
  .contacts svg { flex: none; fill: var(--ink); }

  .band-line { position: absolute; left: 0; bottom: 21px; width: 100%; height: 2px; background: var(--band-line); }
  .band { position: absolute; left: 0; bottom: 0; width: 100%; height: 18px; background: var(--band-black); }
</style>
</head>
<body>
<main class="canvas">

  <section class="card card--front" aria-label="Frente do cartão">
    <div class="monogram">R L F P T</div>
    <p class="profile-link"><span class="icon-square"></span>trabnet.com/in/marianalr</p>
  </section>

  <section class="card card--back" aria-label="Verso do cartão">
    <div class="monogram">R L F P T</div>
    <div class="divider"></div>

    <div class="identity">
      <p class="identity__name">Mariana Lopes</p>
      <p class="identity__surname">F. P. dos Reis</p>
    </div>

    <ul class="contacts">
      <li>
        <svg width="12" height="12" viewBox="0 0 24 24" aria-hidden="true"><path d="M6.6 10.8a15.1 15.1 0 0 0 6.6 6.6l2.2-2.2c.3-.3.7-.4 1-.2 1.1.4 2.3.6 3.6.6.6 0 1 .4 1 1V20c0 .6-.4 1-1 1A17 17 0 0 1 3 4c0-.6.4-1 1-1h3.5c.6 0 1 .4 1 1 0 1.3.2 2.5.6 3.6.1.3 0 .7-.2 1z"/></svg>
        (+55) 61 8493 5710
      </li>
      <li>
        <svg width="12" height="10" viewBox="0 0 24 18" aria-hidden="true"><path d="M0 0h24v2L12 10 0 2zM0 4.5l12 8 12-8V18H0z"/></svg>
        mariana.lop.reis@quellomail.com
      </li>
      <li class="contacts__profile">
        <span class="icon-square"></span>
        trabnet.com/in/marianalr/
      </li>
    </ul>

    <div class="band-line"></div>
    <div class="band"></div>
  </section>

</main>
</body>
</html>
```